New Company Business Card Design

I have a new company logo and I want a new business card design. I dont know if the logo file i attached is in the correct format or quality. We are a New York City Specialty construction Firm specializing in high risk out of the box projects. I want a simple and classy business card that people will his card is as crisp as the work his company does.

Target Market(s)

Clients in the heavy construction industry in New York City

Industry/Entity Type

Construction Company

Contact Information for Business Card

Simple Classy - DIFFERENT

Font styles to use
Other font styles liked:
• Mach the logo font in some way

Colors

Designer to choose colors to be used in the design.

Requirements
Must have
• Uniqueness
Nice to have
• Nothing particular - Just different and classy - Timeless
Should not have
• Goofy Shit or Gimmicky shit

```html
<!DOCTYPE html>
<html lang="en">
<head>
<meta charset="utf-8">
<title>Korvane Associates – Business Card</title>
<link rel="stylesheet" href="https://fonts.googleapis.com/css2?family=Montserrat:wght@500;800&family=Nunito:wght@300&display=swap">
<style>
  :root {
    --stage: #1a1a1a;
    --card: #ffffff;
    --card-shade: #f3f3f3;
    --pattern-tone: #f0f0f0;
    --blue-light: #1aa3e6;
    --blue-deep: #0b4f9c;
    --ink: #1b1b1b;
    --rule: #4a4a4a;
  }
  * { margin: 0; padding: 0; box-sizing: border-box; }
  html, body { width: 1200px; height: 1200px; overflow: hidden; background: var(--stage); }
  .stage { position: relative; width: 1200px; height: 1200px; }

  .card { position: absolute; left: 146px; width: 908px; height: 497px; background: var(--card); overflow: hidden; }
  .card--front { top: 77px; }
  .card--back { top: 630px; height: 498px; }

  .pattern-fill { position: absolute; background: linear-gradient(180deg, var(--pattern-tone), #f8f8f8); }
  .card--front .pattern-fill { left: 0; top: 0; width: 470px; height: 100%; }
  .card--front .shade { position: absolute; left: 470px; top: 0; right: 0; bottom: 0; background: var(--card-shade); }

  .band { position: absolute; left: 0; right: 0; height: 21px; background: linear-gradient(90deg, var(--blue-light), #1a78d2); }
  .band--top { top: 0; }
  .band--bottom { bottom: 0; }

  .brand { position: absolute; text-align: center; font-family: "Montserrat", sans-serif; font-weight: 800; color: var(--blue-deep); line-height: 1; }
  .card--front .brand { left: 0; right: 0; top: 170px; font-size: 96px; letter-spacing: 2px; }
  .card--front .brand small { display: block; font-size: 30px; letter-spacing: 12px; margin-top: 22px; }

  .card--back .pattern-fill { left: 0; top: 0; width: 454px; height: 100%; }
  .card--back .shade { position: absolute; left: 454px; top: 0; right: 0; bottom: 0; background: var(--card-shade); }
  .card--back .brand { left: 85px; width: 246px; top: 212px; font-size: 58px; }
  .card--back .brand small { display: block; font-size: 16px; letter-spacing: 6px; margin-top: 14px; }

  .frame-line { position: absolute; background: var(--rule); }
  .accent-bar { position: absolute; left: 330px; width: 252px; height: 16px; background: linear-gradient(90deg, #0a86d0, var(--blue-deep)); }
  .accent-bar--top { top: 0; }
  .accent-bar--bottom { bottom: 0; }
  .divider { position: absolute; left: 454px; top: 112px; width: 2px; height: 274px; background: var(--ink); }

  .contact { position: absolute; left: 500px; top: 172px; }
  .contact__name { font-family: "Montserrat", sans-serif; font-weight: 500; font-size: 32px; letter-spacing: 1.5px; color: var(--ink); }
  .contact__list { list-style: none; margin-top: 18px; font-family: "Nunito", sans-serif; font-weight: 300; font-size: 17px; color: var(--ink); }
  .contact__list li { display: flex; align-items: flex-start; gap: 8px; margin-bottom: 10px; line-height: 22px; }
  .contact__list svg { width: 18px; height: 18px; flex: none; margin-top: 2px; fill: var(--rule); }
</style>
</head>
<body>
<main class="stage">

  <section class="card card--front">
    <div class="pattern-fill" role="img" aria-label="Faint repeated company-name texture"></div>
    <div class="shade"></div>
    <div class="band band--top"></div>
    <div class="band band--bottom"></div>
    <div class="brand">KORVANE<small>ASSOCIATES, INC.</small></div>
  </section>

  <section class="card card--back">
    <div class="pattern-fill" role="img" aria-label="Faint repeated company-name texture"></div>
    <div class="shade"></div>

    <div class="frame-line" style="left:8px;top:9px;width:310px;height:2px"></div>
    <div class="frame-line" style="left:595px;top:9px;width:305px;height:2px"></div>
    <div class="frame-line" style="left:8px;bottom:10px;width:310px;height:2px"></div>
    <div class="frame-line" style="left:595px;bottom:10px;width:305px;height:2px"></div>
    <div class="frame-line" style="left:8px;top:9px;width:2px;height:480px"></div>
    <div class="frame-line" style="left:898px;top:9px;width:2px;height:480px"></div>
    <div class="accent-bar accent-bar--top"></div>
    <div class="accent-bar accent-bar--bottom"></div>

    <div class="brand">KORVANE<small>ASSOCIATES, INC.</small></div>
    <div class="divider"></div>

    <div class="contact">
      <h1 class="contact__name">MARCUS T. BELLWOOD</h1>
      <ul class="contact__list">
        <li><svg viewBox="0 0 24 24"><path d="M6.6 10.8a15 15 0 0 0 6.6 6.6l2.2-2.2a1 1 0 0 1 1-.25 11.4 11.4 0 0 0 3.6.57 1 1 0 0 1 1 1V20a1 1 0 0 1-1 1A17 17 0 0 1 3 4a1 1 0 0 1 1-1h3.5a1 1 0 0 1 1 1c0 1.25.2 2.45.57 3.57a1 1 0 0 1-.25 1z"/></svg>555-014-2287</li>
        <li><svg viewBox="0 0 24 24"><path d="M2 5h20v14H2z M4 7v.4l8 5.2 8-5.2V7l-8 5.2z" fill-rule="evenodd"/></svg>marcus@korvane.com</li>
        <li><svg viewBox="0 0 24 24"><path d="M12 2a7 7 0 0 0-7 7c0 5.2 7 13 7 13s7-7.8 7-13a7 7 0 0 0-7-7zm0 9.5A2.5 2.5 0 1 1 12 6.5a2.5 2.5 0 0 1 0 5z"/></svg><span>412 Dockside Avenue -<br>Bayport, New Jersey 07190</span></li>
      </ul>
    </div>
  </section>

</main>
</body>
</html>
```